Northwind Crate Traders Needs a FRESH website

We would like a creative minded designer to take on the task to Re-design our website. Its a simple 5-7 pages. With no cart, no complex html. Just plain information about our company and products we import and export. Pictures added to the product section. Since Our logo its Blue, we would like the designer to use complementing colors in order to make the website look cleaner and modern.

Target Market(s)

The target audience will be companies looking to purchase plastic related products. Companies looking to purchase large quantities of plastic containers (Shampoo bottles, caps, sprayers, mist sprayers, cosmetic containers etc).

Industry/Entity Type

It Company

Font styles to use
Sans Serif

Requirements
Must have
• We have a section in which we would like to add pictures of some of the products we carry, therefore having an easy and clean way to navigate through the pictures will be a plus.

```html
<!DOCTYPE html>
<html lang="en">
<head>
<meta charset="utf-8">
<title>Northwind Crate Traders</title>
<link rel="stylesheet" href="https://fonts.googleapis.com/css2?family=Source+Sans+3:wght@300;400;600;700&family=Ubuntu:wght@300;400&display=swap">
<style>
:root{
  --blue:#1a93dc;
  --blue-dark:#0f7fc4;
  --nav-text:#1f5f8c;
  --ink:#333a40;
  --muted:#9aa5ad;
  --line:#dfe3e6;
  --hero-top:#eaf6fd;
  --hero-mid:#bfe4f7;
  --footer:#0d8fdc;
  --white:#ffffff;
}
*{box-sizing:border-box;margin:0;padding:0}
html,body{width:1024px;height:1200px;overflow:hidden}
body{position:relative;background:#f7f9fa;font-family:"Source Sans 3",sans-serif;color:var(--ink)}
.abs{position:absolute}

/* header */
.topbar{left:0;top:0;width:1024px;height:56px;background:var(--white)}
.contact-strip{top:22px;font-size:10px;color:var(--blue-dark);display:flex;align-items:center;gap:6px;white-space:nowrap}
.navband{left:0;top:56px;width:1024px;height:40px;background:linear-gradient(#4eaee6,#2b92d6);border-top:1px solid #7cc5ef;border-bottom:1px solid #1f7ec0}
.nav{position:absolute;left:457px;top:0;display:flex;height:40px}
.nav a{display:flex;align-items:center;justify-content:center;height:40px;font-size:11px;font-weight:600;color:var(--nav-text);text-decoration:none;border-left:1px solid #2a83c3;border-right:1px solid #6fbdec}
.nav a.active{background:#2a86c9;color:var(--white)}
.brand{left:136px;top:0;width:152px;height:120px;background:linear-gradient(#ffffff,#f0f2f3);box-shadow:0 1px 3px rgba(0,0,0,.2);display:flex;flex-direction:column;align-items:center;justify-content:center;gap:8px;z-index:3}
.brand-dot{width:40px;height:40px;border-radius:50%;background:var(--blue)}
.brand-name{font-size:15px;font-weight:600;color:var(--blue);text-align:center;line-height:1.15}

/* hero */
.hero{left:0;top:96px;width:1024px;height:608px;background:linear-gradient(160deg,var(--hero-top) 0%,#d6eefa 45%,var(--hero-mid) 100%);overflow:hidden}
.hero-visual{left:0;top:0;width:1024px;height:608px;background:linear-gradient(100deg,#6ab2da 0%,#9fd2ee 38%,rgba(214,238,250,0) 62%)}
.hero-title{right:132px;top:146px;font-family:"Ubuntu",sans-serif;font-weight:300;font-size:29px;color:#3a4248;text-align:right;white-space:nowrap}
.hero-lead{right:132px;top:193px;width:310px;font-size:12.5px;line-height:19px;color:#1d7fc0;text-align:right}
.btn-primary{left:777px;top:275px;width:112px;height:36px;background:linear-gradient(#43aaea,#1b8ad3);border:1px solid #1478bd;border-radius:2px;color:var(--white);font-size:12.5px;font-weight:600;display:flex;align-items:center;justify-content:center}
.dots{left:828px;top:424px;display:flex;gap:4px}
.dots span{width:9px;height:9px;border-radius:50%;background:#8fd0f0}
.dots span.on{background:var(--blue)}

/* cards */
.card{top:570px;width:240px;height:289px;background:var(--white);border:1px solid var(--line);box-shadow:0 1px 2px rgba(0,0,0,.06)}
.card h2{font-family:"Ubuntu",sans-serif;font-weight:400;font-size:14px;text-align:center;margin-top:20px;color:#333;white-space:nowrap}
.card h2 em{font-style:normal;color:var(--blue)}
.card-image{margin:8px auto 0;width:216px;height:112px}
.card p{margin:18px 11px 0;font-size:9.6px;line-height:16px;color:var(--muted)}
.btn-ghost{margin:17px 0 0 12px;width:88px;height:30px;border:1px solid #c9ced2;border-radius:15px;background:linear-gradient(#fff,#eef0f1);font-size:9.5px;color:#7a858c;display:flex;align-items:center;justify-content:center;gap:5px}
.card-contact{left:649px;top:570px;width:240px;height:289px;background:var(--white);border:1px solid var(--line)}
.contact-head{height:95px;background:linear-gradient(#3aa8e8,#1590d8);position:relative}
.contact-icon{position:absolute;left:13px;top:22px;width:51px;height:51px;border-radius:3px;background:#1a86cb;box-shadow:inset 0 0 0 1px #56b6ec;display:flex;align-items:center;justify-content:center}
.contact-head h3{position:absolute;left:79px;top:22px;font-family:"Ubuntu",sans-serif;font-weight:300;font-size:19px;color:var(--white)}
.contact-head p{position:absolute;left:80px;top:55px;width:150px;font-size:9.5px;line-height:14px;color:#d9efff}
.contact-row{height:39px;border-bottom:1px solid var(--line);padding:0 20px;display:flex;align-items:center;font-size:13px;color:#a2abb1;font-weight:300;white-space:nowrap}
.contact-row span{color:var(--blue);margin-left:3px}
.address{padding:26px 20px 0;font-size:9.5px;line-height:23px;color:#a2abb1}

/* services */
.service{width:180px}
.service-head{display:flex;align-items:center;gap:8px}
.service-icon{width:32px;height:32px;border-radius:50%;background:var(--blue);box-shadow:0 0 0 2px #bfe3f7;display:flex;align-items:center;justify-content:center;flex:none}
.service h4{font-size:11.5px;font-weight:600;color:#3b4349}
.service p{margin:9px 0 0 1px;font-size:10.5px;line-height:16px;color:var(--muted)}

/* footer */
.footer{left:0;top:1126px;width:1024px;height:74px;background:var(--footer);color:var(--white)}
.footer-links{left:145px;top:19px;font-size:9px;font-weight:700;letter-spacing:.3px}
.footer-copy{left:143px;top:44px;font-size:9px;font-weight:600}
.social{top:15px;width:22px;height:22px;border-radius:50%;background:var(--white)}
.footer-contact{left:715px;font-size:9px;font-weight:700;display:flex;align-items:center;gap:12px}
</style>
</head>
<body>

<header>
  <div class="abs topbar"></div>
  <div class="abs contact-strip" style="left:648px">
    <svg width="22" height="12" viewBox="0 0 22 12"><path d="M0 3h5M1 6h4M2 9h3" stroke="#7aaecc" stroke-width="1"/><rect x="7" y="1" width="14" height="10" fill="none" stroke="#4a9bd0" stroke-width="1"/><path d="M7 1l7 6 7-6" fill="none" stroke="#4a9bd0" stroke-width="1"/></svg>
    info@northwindcrate.com
  </div>
  <div class="abs contact-strip" style="left:808px">
    <svg width="13" height="13" viewBox="0 0 13 13"><path d="M3 1l2 3-1.5 1.5c.8 1.8 2.2 3.2 4 4L9 8l3 2-1 2.5C6 12 1 7 .5 2z" fill="none" stroke="#4a9bd0" stroke-width="1"/></svg>
    +84 910 442 317
  </div>
  <div class="abs navband">
    <nav class="nav">
      <a class="active" style="width:72px">Home</a>
      <a style="width:72px">About</a>
      <a style="width:72px">Products</a>
      <a style="width:144px">Mission Statement</a>
      <a style="width:72px">Contact</a>
    </nav>
  </div>
  <div class="abs brand">
    <div class="brand-dot"></div>
    <div class="brand-name">Northwind<br>Crate Traders</div>
  </div>
</header>

<section class="abs hero">
  <div class="abs hero-visual" role="img" aria-label="Smiling businesswoman in a grey suit beside blurred freight trucks and a globe on a light blue background"></div>
  <h1 class="abs hero-title">At Northwind Crate Traders</h1>
  <p class="abs hero-lead">We make it our priority delivering an extensive and top of the line supply portfolio of most products related to the plastic industry.</p>
  <div class="abs btn-primary">Contact Us</div>
  <div class="abs dots"><span class="on"></span><span></span><span></span><span></span></div>
</section>

<article class="abs card" style="left:136px">
  <h2>About <em>Northwind Crate Traders</em></h2>
  <div class="card-image" role="img" aria-label="Business team discussing documents at a table" style="background:linear-gradient(135deg,#cfe3ee,#6f8796 55%,#2e3338)"></div>
  <p>Lorem ipsum dolor sit amet, consectetur adipisicing elit, sed do eiusmod tempor incididunt ut labore et dolore magna aliqua.</p>
  <div class="btn-ghost">Read More <span>›</span></div>
</article>

<article class="abs card" style="left:393px">
  <h2>Our <em>Products</em></h2>
  <div class="card-image" role="img" aria-label="Steel injection mould for plastic containers" style="background:linear-gradient(135deg,#5d7c97,#c7ccd0 45%,#8d949a)"></div>
  <p>Lorem ipsum dolor sit amet, consectetur adipisicing elit, sed do eiusmod tempor incididunt ut labore et dolore magna aliqua.</p>
  <div class="btn-ghost">Read More <span>›</span></div>
</article>

<aside class="abs card-contact">
  <div class="contact-head">
    <div class="contact-icon">
      <svg width="28" height="22" viewBox="0 0 28 22"><ellipse cx="12" cy="9" rx="11" ry="7.5" fill="#fff"/><path d="M5 14l-2 6 7-4z" fill="#fff"/><ellipse cx="18" cy="12" rx="9" ry="6" fill="#dcefff"/></svg>
    </div>
    <h3>Questions?</h3>
    <p>If you have inquiries, please don't hesitate to contact us.</p>
  </div>
  <div class="contact-row">Phone: (+39) 2406183374</div>
  <div class="contact-row" style="height:42px">E-mail:<span>info@northwindcrate.com</span></div>
  <div class="address">Northwind Crate Traders<br>4418 Harbor Lane<br>Bayview Flats - Oakland, USA</div>
</aside>

<section>
  <div class="abs service" style="left:137px;top:886px">
    <div class="service-head"><div class="service-icon"><svg width="16" height="14" viewBox="0 0 16 14"><ellipse cx="8" cy="6" rx="7" ry="5" fill="#fff"/><path d="M4 10l-1 4 4-3z" fill="#fff"/></svg></div><h4>Product Research</h4></div>
    <p>Lorem ipsum dolor sit amet, tetur adipiscing elit. Suspendisse smod congue bibendum.</p>
  </div>
  <div class="abs service" style="left:329px;top:886px">
    <div class="service-head"><div class="service-icon"><svg width="16" height="16" viewBox="0 0 16 16"><rect x="3" y="3" width="10" height="10" fill="none" stroke="#fff" stroke-width="1.5"/><path d="M1 3h4M11 3h4M1 13h4M11 13h4" stroke="#fff" stroke-width="1.5"/></svg></div><h4>OEM / ODM</h4></div>
    <p>Lorem ipsum dolor sit amet, tetur adipiscing elit. Suspendisse smod congue bibendum.</p>
  </div>
  <div class="abs service" style="left:521px;top:886px">
    <div class="service-head"><div class="service-icon"><svg width="18" height="18" viewBox="0 0 18 18"><circle cx="9" cy="9" r="7" fill="none" stroke="#fff" stroke-width="1.5"/><path d="M2 9h14M9 2c-3 4-3 10 0 14M9 2c3 4 3 10 0 14" fill="none" stroke="#fff" stroke-width="1"/></svg></div><h4>Delivery</h4></div>
    <p>Lorem ipsum dolor sit amet, tetur adipiscing elit. Suspendisse smod congue bibendum.</p>
  </div>
  <div class="abs service" style="left:713px;top:886px">
    <div class="service-head"><div class="service-icon"><svg width="16" height="16" viewBox="0 0 16 16"><path d="M6 2h4M7 2v5l-4 7h10l-4-7V2" fill="#fff" stroke="#fff" stroke-width="1.2" stroke-linejoin="round"/></svg></div><h4>Freight Forwarding</h4></div>
    <p>Lorem ipsum dolor sit amet, tetur adipiscing elit. Suspendisse smod congue bibendum.</p>
  </div>

  <div class="abs service" style="left:137px;top:1003px">
    <div class="service-head"><div class="service-icon"><svg width="14" height="16" viewBox="0 0 14 16"><path d="M2 1h7l3 3v11H2z" fill="none" stroke="#fff" stroke-width="1.4"/><circle cx="7" cy="10" r="2" fill="none" stroke="#fff" stroke-width="1.2"/></svg></div><h4>Packaging</h4></div>
    <p>Lorem ipsum dolor sit amet, tetur adipiscing elit. Suspendisse smod congue bibendum.</p>
  </div>
  <div class="abs service" style="left:329px;top:1003px">
    <div class="service-head"><div class="service-icon"><svg width="16" height="16" viewBox="0 0 16 16"><path d="M14 2L6 11l-1 3 3-1 8-9z" fill="#fff"/><path d="M2 14c1-2 2-2 3-1" stroke="#fff" stroke-width="1.4" fill="none"/></svg></div><h4>Product Design</h4></div>
    <p>Lorem ipsum dolor sit amet, tetur adipiscing elit. Suspendisse smod congue bibendum.</p>
  </div>
  <div class="abs service" style="left:521px;top:1003px">
    <div class="service-head"><div class="service-icon"><svg width="16" height="16" viewBox="0 0 16 16"><path d="M8 1l7 7-7 7-7-7z" fill="none" stroke="#fff" stroke-width="1.6"/><circle cx="8" cy="5" r="1.3" fill="#fff"/></svg></div><h4>Labeling</h4></div>
    <p>Lorem ipsum dolor sit amet, tetur adipiscing elit. Suspendisse smod congue bibendum.</p>
  </div>
  <div class="abs service" style="left:713px;top:1003px">
    <div class="service-head"><div class="service-icon"><svg width="16" height="16" viewBox="0 0 16 16"><path d="M3 2v12M6.5 2v12M9.5 2v12M13 2v12" stroke="#fff" stroke-width="1.3"/><path d="M1.5 6h3M5 10h3M8 5h3M11.5 9h3" stroke="#fff" stroke-width="2"/></svg></div><h4>Custom</h4></div>
    <p>Lorem ipsum dolor sit amet, tetur adipiscing elit. Suspendisse smod congue bibendum.</p>
  </div>
</section>

<footer class="abs footer">
  <div class="abs footer-links">LINKS &nbsp;| &nbsp;LINKS &nbsp;| &nbsp;LINKS &nbsp;| &nbsp;LINKS</div>
  <div class="abs footer-copy">Copyright © 2014. All rights reserved. &nbsp;Company Name. Privacy Policy &nbsp;| &nbsp;Sitemap</div>
  <div class="abs social" style="left:591px"></div>
  <div class="abs social" style="left:623px"></div>
  <div class="abs social" style="left:654px"></div>
  <div class="abs footer-contact" style="top:15px">
    <svg width="16" height="12" viewBox="0 0 16 12"><rect width="16" height="12" fill="#9fd3f3"/><path d="M0 0l8 6 8-6" fill="none" stroke="#0d8fdc" stroke-width="1.2"/></svg>
    hello@northwindcrate.com
  </div>
  <div class="abs footer-contact" style="top:39px">
    <svg width="16" height="14" viewBox="0 0 13 13"><path d="M3 1l2 3-1.5 1.5c.8 1.8 2.2 3.2 4 4L9 8l3 2-1 2.5C6 12 1 7 .5 2z" fill="#9fd3f3"/></svg>
    890-07215-33841
  </div>
</footer>

</body>
</html>
```